Ready to eat rice packaging design

We need packaging design for pre cooked rice of different types
1. Basmati Rice
2. Brown basmati Rice
3. Jasmine Rice
4. Lemon Rice
5. Rice Pilaf
6. Biryani Rice

Back of the package will have preparation write up and Nutrition chart.

The design should have both natural as well as modern feel to it.

Examples of packages available in market enclosed.

Target Market(s)

National Food and Grocery Stores in USA

Industry/Entity Type

Grocery Store

```html
<!DOCTYPE html>
<html lang="en">
<head>
<meta charset="UTF-8">
<title>Jasmine Rice – Pouch Front</title>
<link rel="stylesheet" href="https://fonts.googleapis.com/css2?family=Comfortaa:wght@700&family=Crimson+Text:wght@400;600&display=swap">
<style>
  :root{
    --stage:#1a1a1a;
    --purple:#8a2fa6;
    --purple-deep:#6a1d84;
    --purple-light:#a548c2;
    --brown:#3e2317;
    --brown-soft:#4a2a1c;
    --gold:#d39a3a;
    --gold-light:#f1c56a;
    --lavender:#c98ee0;
    --white:#ffffff;
    --cream:#f3ece4;
  }
  *{margin:0;padding:0;box-sizing:border-box;}
  html,body{width:800px;height:1200px;overflow:hidden;background:var(--stage);}
  .canvas{position:relative;width:800px;height:1200px;}
  .pouch{
    position:absolute;left:80px;top:80px;width:640px;height:1040px;
    background:linear-gradient(90deg,var(--purple-deep) 0%,var(--purple) 12%,var(--purple-light) 40%,var(--purple) 75%,var(--purple-deep) 100%);
    border-radius:6px;overflow:hidden;
  }
  .zip-line{position:absolute;left:0;right:0;top:72px;height:2px;background:rgba(0,0,0,.25);}
  .zip-line.second{top:80px;background:rgba(255,255,255,.12);}
  .center-band{
    position:absolute;left:160px;top:4px;width:330px;height:1020px;
    background:var(--brown);
    border:3px solid var(--gold);border-radius:14px;
  }
  .band-pattern{position:absolute;inset:0;border-radius:12px;
    background:linear-gradient(180deg,var(--brown-soft),var(--brown) 50%,var(--brown-soft));}
  .logo-arch{
    position:absolute;left:240px;top:210px;width:176px;height:190px;
    border:3px solid var(--gold);border-radius:88px 88px 0 0;
    display:flex;align-items:center;justify-content:center;padding-top:36px;
  }
  .logo-name{font-family:'Crimson Text',serif;font-size:52px;color:var(--white);}
  .product-name{
    position:absolute;left:160px;width:330px;text-align:center;
    font-family:'Comfortaa',sans-serif;font-weight:700;color:var(--lavender);
    -webkit-text-stroke:1.5px var(--white);letter-spacing:-1px;
  }
  .product-name.line-one{top:425px;font-size:62px;}
  .product-name.line-two{top:516px;font-size:62px;}
  .name-rule{position:absolute;left:192px;top:512px;width:266px;height:2px;background:var(--cream);}
  .tagline{
    position:absolute;left:160px;top:592px;width:330px;text-align:center;
    font-family:'Crimson Text',serif;font-size:36px;color:var(--cream);
  }
  .serving-window{
    position:absolute;left:110px;top:645px;width:450px;height:290px;
    border:3px solid var(--gold);border-radius:14px;
    background:radial-gradient(ellipse at 50% 58%,#f4f1ec 0%,#dcdad8 28%,#a9a9ab 60%,#8b8b8e 100%);
  }
  .net-weight{
    position:absolute;left:160px;top:948px;width:330px;text-align:center;
    font-family:'Crimson Text',serif;font-weight:600;font-size:17px;color:var(--cream);
  }
</style>
</head>
<body>
<div class="canvas">
  <div class="pouch">
    <div class="zip-line"></div>
    <div class="zip-line second"></div>
    <div class="center-band">
      <div class="band-pattern" role="img" aria-label="Repeating lotus motif pattern in dark brown"></div>
    </div>
    <div class="logo-arch"><span class="logo-name">Logo</span></div>
    <div class="product-name line-one">Jasmine</div>
    <div class="name-rule"></div>
    <div class="product-name line-two">rice</div>
    <div class="tagline">Premium Rice</div>
    <div class="serving-window" role="img" aria-label="Plate of fluffy white jasmine rice with peas, diced peppers and a mint sprig"></div>
    <div class="net-weight">Net Wt. 1 Kg.</div>
  </div>
</div>
</body>
</html>
```